Logo and Flyer for Co-Branded Comedy Show

Graphic designer needed to create a promotional flyer for a comedy show. Two different comedy shows, with distinct branding, are joining forces to create a combined show. (co-branded logo to be included is attached.)

The design of the promotional materials should be a modern take on a vintage poster a la Quirkwood Jamboree. We'd like it to be a vintage look with a modern twist (I have attached the Quirkwood Jamboree Flyer for reference - marked up with info for our show) Filename: PLGRVN Flyer Mark Up

Images of the two hosts are attached: Filenames:

Our show will be in a theater, so if it can play off a playbill that would be great. I have attached examples of the clean look that we like, as well as some vintage theater flyers. We'd like to stay on the lighter side of the color palette (light gray, blues, etc. which is in line with the Harbor Laughs Live flyer) Filename: PLGR VN Flyer Direction

Current Branding of the individual Shows
I have attached the current promo materials for the individual shows, so you have a sense of the color palette and logo treatment.

The deliverable:
1 flyer vertical, 1 flyer horizontal - same design/concept but in 2 orientation (vertical and horizontal) horizontal will be used for web.
***This flyer will include the co-branded logo seen attached - Harbor Laughs Live Gets Real Honest (individual logos already created and attached) - Download PSD File here: http://lnk.example-short.test/PLGRVN

Industry/Entity Type

Graphic Designer

Colors
0493cd
85cae6
ecf7fb
f5f5f5
ffffff
606060
fbfbfb
0255a3
3176b5

Requirements
Must have
• Vintage look with a modern twist
• Vertical and horizontal options

```html
<!DOCTYPE html>
<html lang="en">
<head>
<meta charset="utf-8">
<title>Harbor Laughs Live Gets Real Honest — Comedy Show Flyer</title>
<link rel="stylesheet" href="https://fonts.googleapis.com/css2?family=Alfa+Slab+One&family=Bebas+Neue&family=Oswald:wght@400;600;700&display=swap">
<style>
  :root {
    --sky: #2fb0e2;
    --sky-deep: #0493cd;
    --sky-edge: #0a6fa8;
    --navy: #0d2a48;
    --ink: #14263a;
    --white: #ffffff;
    --paper: #ecf7fb;
    --photo-a: #5a4a42;
    --photo-b: #2b2f38;
  }
  * { margin: 0; padding: 0; box-sizing: border-box; }
  html, body { width: 778px; height: 1200px; overflow: hidden; background: var(--white); }
  .flyer {
    position: relative;
    width: 778px; height: 1200px;
    background: radial-gradient(ellipse at 50% 45%, var(--sky) 0%, var(--sky-deep) 70%, var(--sky-edge) 100%);
    color: var(--navy);
    text-align: center;
    font-family: "Oswald", sans-serif;
    overflow: hidden;
  }
  .frame {
    position: absolute; inset: 16px;
    border: 3px solid var(--navy);
    pointer-events: none;
  }
  .presenter {
    position: absolute; top: 34px; left: 0; right: 0;
    font-family: "Bebas Neue", sans-serif;
    font-size: 30px; letter-spacing: 2px; color: var(--white);
  }
  .presenter .dot {
    display: inline-block; width: 14px; height: 14px; border-radius: 50%;
    background: var(--white); margin-right: 8px; vertical-align: 2px;
  }
  .presents {
    position: absolute; top: 72px; left: 0; right: 0;
    font-family: "Oswald", sans-serif; font-weight: 600;
    font-size: 18px; letter-spacing: 5px; color: var(--navy);
  }
  .title { position: absolute; top: 110px; left: 0; right: 0; font-family: "Alfa Slab One", serif; line-height: 1; color: var(--navy); }
  .title .line-1 { font-size: 104px; letter-spacing: 2px; }
  .title .line-2 { font-size: 50px; margin-top: 10px; letter-spacing: 1px; }
  .title .line-2 .accent { color: var(--white); }
  .title .line-3 { font-size: 104px; margin-top: 10px; letter-spacing: 3px; }
  .tagline {
    position: absolute; top: 418px; left: 0; right: 0;
    font-family: "Oswald", sans-serif; font-weight: 600;
    font-size: 20px; letter-spacing: 4px; color: var(--navy);
  }
  .tagline::before, .tagline::after {
    content: ""; display: inline-block; width: 90px; height: 2px;
    background: var(--navy); vertical-align: middle; margin: 0 16px;
  }
  .lineup { position: absolute; top: 462px; left: 0; right: 0; height: 270px; }
  .act { position: absolute; text-align: center; }
  .act .role {
    display: inline-block; background: var(--navy); color: var(--white);
    font-family: "Bebas Neue", sans-serif; font-size: 20px; letter-spacing: 2px;
    padding: 3px 16px 1px;
  }
  .act .photo {
    display: block; margin: 10px auto 0; border-radius: 50%;
    border: 5px solid var(--white);
    background: radial-gradient(circle at 50% 40%, var(--photo-a), var(--photo-b));
  }
  .act .name {
    display: inline-block; background: var(--white); color: var(--navy);
    font-family: "Bebas Neue", sans-serif; letter-spacing: 1px;
    margin-top: -14px; position: relative; padding: 2px 12px 0;
  }
  .act .credit {
    display: block; font-size: 11px; letter-spacing: 1px; color: var(--white); margin-top: 3px;
  }
  .act.co-left { left: 120px; width: 200px; top: 18px; }
  .act.co-right { right: 120px; width: 200px; top: 18px; }
  .act.co-left .photo, .act.co-right .photo { width: 160px; height: 160px; }
  .act.co-left .name, .act.co-right .name { font-size: 20px; }
  .act.headliner { left: 264px; width: 250px; top: 0; }
  .act.headliner .photo { width: 220px; height: 220px; }
  .act.headliner .name { font-size: 34px; padding: 2px 20px 0; }
  .featuring {
    position: absolute; top: 752px; left: 0; right: 0;
    font-family: "Bebas Neue", sans-serif; font-size: 26px; letter-spacing: 4px; color: var(--white);
  }
  .roster {
    position: absolute; top: 790px; left: 90px; right: 90px;
    font-family: "Oswald", sans-serif; font-weight: 600; font-size: 19px;
    letter-spacing: 1px; line-height: 1.55; color: var(--navy);
  }
  .roster .sep { color: var(--white); margin: 0 6px; }
  .one-night {
    position: absolute; top: 870px; left: 0; right: 0;
    font-family: "Alfa Slab One", serif; font-size: 30px; letter-spacing: 2px; color: var(--white);
  }
  .date {
    position: absolute; top: 910px; left: 0; right: 0;
    font-family: "Bebas Neue", sans-serif; font-size: 78px; letter-spacing: 2px; color: var(--navy); line-height: 1;
  }
  .venue {
    position: absolute; top: 990px; left: 0; right: 0;
    display: flex; justify-content: center; align-items: center; gap: 16px;
  }
  .venue .place { font-family: "Alfa Slab One", serif; font-size: 56px; color: var(--white); line-height: 1; }
  .venue .address {
    text-align: left; font-family: "Oswald", sans-serif; font-weight: 600;
    font-size: 15px; letter-spacing: 1px; line-height: 1.3; color: var(--navy);
  }
  .footer {
    position: absolute; bottom: 42px; left: 50px; right: 50px;
    display: flex; align-items: center; justify-content: space-between;
  }
  .show-mark { display: flex; align-items: center; gap: 8px; width: 130px; }
  .show-mark .disc { width: 18px; height: 18px; border-radius: 50%; background: var(--navy); flex: none; }
  .show-mark .label {
    font-family: "Oswald", sans-serif; font-weight: 600; font-size: 15px;
    line-height: 1.1; color: var(--navy); text-align: left; text-transform: uppercase;
  }
  .tickets { text-align: center; color: var(--navy); }
  .tickets .lead { font-size: 13px; letter-spacing: 2px; font-weight: 600; }
  .tickets .url { font-family: "Alfa Slab One", serif; font-size: 30px; color: var(--white); }
</style>
</head>
<body>
<main class="flyer">
  <div class="frame"></div>

  <div class="presenter"><span class="dot"></span>NORTHLIGHT ENTERTAINMENT</div>
  <div class="presents">PRESENTS</div>

  <h1 class="title">
    <div class="line-1">HARBOR</div>
    <div class="line-2">LAUGHS LIVE <span class="accent">GETS REAL</span></div>
    <div class="line-3">HONEST</div>
  </h1>

  <div class="tagline">AN ALL STAR COMEDY SHOW</div>

  <section class="lineup">
    <div class="act co-left">
      <span class="role">CO-HOST</span>
      <span class="photo" role="img" aria-label="Portrait photo of co-host Zolo Brightwave"></span>
      <span class="name">ZOLO BRIGHTWAVE</span>
      <span class="credit">RADIO SHOW HOST</span>
    </div>
    <div class="act headliner">
      <span class="role">HEADLINER</span>
      <span class="photo" role="img" aria-label="Portrait photo of headliner Delmar Okafor"></span>
      <span class="name">DELMAR OKAFOR</span>
    </div>
    <div class="act co-right">
      <span class="role">CO-HOST</span>
      <span class="photo" role="img" aria-label="Portrait photo of co-host Marla Vintrow"></span>
      <span class="name">MARLA VINTROW</span>
      <span class="credit">COMEDY WRITER</span>
    </div>
  </section>

  <div class="featuring">FEATURING</div>
  <div class="roster">
    RAVI TOLLMAN<span class="sep">·</span>PERCY LINDQVIST<span class="sep">·</span>OWEN BARROWCLIFF<br>
    NINA KOVAL<span class="sep">·</span>DELMAR OKAFOR<span class="sep">·</span>TEDDY HALVORSEN<span class="sep">·</span>&amp; MORE
  </div>

  <div class="one-night">ONE NIGHT</div>
  <div class="date">SATURDAY, AUGUST 22, 2015</div>

  <div class="venue">
    <span class="place">@ VESPER HALL</span>
    <span class="address">214 HARBOR AVENUE<br>BAYPORT, NY 10099</span>
  </div>

  <footer class="footer">
    <div class="show-mark"><span class="disc"></span><span class="label">Harbor Laughs Live</span></div>
    <div class="tickets">
      <div class="lead">FOR TICKETS AND ADDITIONAL INFO VISIT:</div>
      <div class="url">WWW.PLGRVN.EXAMPLE</div>
    </div>
    <div class="show-mark"><span class="disc"></span><span class="label">Gets Real Honest</span></div>
  </footer>
</main>
</body>
</html>
```